Debt Relief Landing Page Design

I need a landing page designed (and the accompanying Thank You page) for my client.

I have drafted the wireframes for the layout of the pages (attached) and need a professional looking finish.

The main colours to use are green and blue as per their current branding, see website for specifications - http://www.clearpathledger.com.au/

Industry/Entity Type

Debt

Coding

Coded - Design and coding required

```html
<!DOCTYPE html>
<html lang="en">
<head>
<meta charset="utf-8">
<title>Clear Path Ledger – Debt Consolidation</title>
<link href="https://fonts.googleapis.com/css2?family=Open+Sans:wght@400;600;700&display=swap" rel="stylesheet">
<style>
:root{
  --navy:#1e2d59;
  --navy-dark:#17224a;
  --green:#4f9a2c;
  --ink:#333a48;
  --muted:#6b7280;
  --line:#d9dde3;
  --bg-soft:#eef0f3;
  --white:#ffffff;
}
*{box-sizing:border-box;margin:0;padding:0}
html,body{width:1200px;height:2552px;overflow:hidden}
body{font-family:"Open Sans",Arial,sans-serif;color:var(--ink);background:var(--white);position:relative}
.site-header{height:88px;display:flex;align-items:center;justify-content:space-between;padding:0 100px;border-bottom:1px solid var(--line)}
.brand{display:flex;align-items:center;gap:10px;font-size:30px;font-weight:700;color:var(--navy)}
.brand-mark{width:14px;height:14px;background:var(--green)}
.contact{text-align:right}
.contact small{display:block;font-size:12px;color:var(--muted)}
.contact .phone{display:flex;align-items:center;gap:8px;font-size:24px;font-weight:700;color:var(--navy)}
.hero{position:absolute;top:88px;left:0;width:1200px;height:852px;background:var(--bg-soft)}
.hero-copy{position:absolute;left:100px;top:40px;width:600px}
.hero-copy h2{font-size:19px;font-weight:700;color:var(--navy);margin-bottom:40px}
.hero-copy h1{font-size:27px;font-weight:400;line-height:1.35;color:var(--navy);margin-bottom:26px}
.hero-copy p{font-size:13px;line-height:1.7;color:var(--muted);margin-bottom:18px}
.lead-form{position:absolute;right:100px;top:40px;width:330px;background:var(--white);border:1px solid var(--line)}
.lead-form header{background:var(--navy);color:var(--white);padding:22px 24px;text-align:center}
.lead-form header h3{font-size:15px;font-weight:700;letter-spacing:.5px}
.lead-form header p{font-size:11px;line-height:1.5;margin-top:6px;opacity:.85}
.fields{padding:20px 22px 26px;background:var(--navy)}
.field{height:40px;background:var(--white);margin-bottom:12px;display:flex;align-items:center;padding:0 12px;gap:10px;font-size:12px;color:var(--muted)}
.field svg{flex:none}
.btn{display:inline-block;background:var(--green);color:var(--white);font-size:13px;font-weight:700;letter-spacing:.4px;text-transform:uppercase;padding:15px 28px;text-align:center}
.lead-form .btn{width:100%;margin-top:8px}
.section-title{text-align:center;font-size:27px;font-weight:400;color:var(--navy)}
.services{position:absolute;top:940px;left:0;width:1200px;height:680px;background:var(--white)}
.services .section-title{margin-top:68px}
.service-grid{display:grid;grid-template-columns:repeat(3,300px);column-gap:50px;row-gap:60px;justify-content:center;margin-top:70px}
.service{text-align:center}
.service svg{display:block;margin:0 auto 14px}
.service h4{font-size:16px;font-weight:600;color:var(--navy);margin-bottom:10px}
.service p{font-size:12px;line-height:1.6;color:var(--muted)}
.services .cta,.reviews .cta{position:absolute;left:50%;transform:translateX(-50%)}
.services .cta{top:580px}
.reviews{position:absolute;top:1620px;left:0;width:1200px;height:852px;background:var(--bg-soft)}
.reviews .section-title{margin-top:40px}
.review-grid{display:grid;grid-template-columns:repeat(3,300px);column-gap:50px;row-gap:40px;justify-content:center;margin-top:50px}
.review{position:relative;padding-left:34px}
.review .quote{position:absolute;left:0;top:-6px;font-size:44px;font-weight:700;color:var(--navy);line-height:1}
.review p{font-size:12px;line-height:1.65;color:var(--muted);height:160px}
.reviewer{display:flex;align-items:center;gap:14px;margin-top:16px;font-size:12px;color:var(--navy);font-weight:600}
.avatar{width:46px;height:46px;border-radius:50%;background:linear-gradient(135deg,#b9c1cc,#8c96a5)}
.reviews .cta{top:748px}
.site-footer{position:absolute;top:2472px;left:0;width:1200px;height:80px;background:var(--navy-dark);color:var(--white);display:flex;align-items:center;justify-content:center;gap:14px;font-size:11px;font-weight:600;letter-spacing:.4px}
</style>
</head>
<body>
<header class="site-header">
  <div class="brand"><span class="brand-mark"></span>Clear Path Ledger</div>
  <div class="contact">
    <small>Contact us on</small>
    <div class="phone">
      <svg width="20" height="20" viewBox="0 0 24 24"><path fill="#1e2d59" d="M6.6 10.8a15.1 15.1 0 0 0 6.6 6.6l2.2-2.2a1 1 0 0 1 1-.25 11.4 11.4 0 0 0 3.6.57 1 1 0 0 1 1 1V20a1 1 0 0 1-1 1A17 17 0 0 1 3 4a1 1 0 0 1 1-1h3.5a1 1 0 0 1 1 1c0 1.25.2 2.45.57 3.57a1 1 0 0 1-.25 1z"/></svg>
      1300 555 014
    </div>
  </div>
</header>

<section class="hero">
  <div class="hero-copy">
    <h2>Looking to Consolidate your debts?</h2>
    <h1>If you have over $10,000 in debt,<br>we can help you be debt free in 3-5 Years.</h1>
    <p>Ledger Advisors is Australia's debt help relief specialists. Through years of industry experience and knowledge, our team of debt management experts can actively advise you on how to get out of the red, fast.</p>
    <p>At Ledger Advisors we are able to actively rectify your debt problems by creating simple and affordable payment plans for all clients.</p>
    <p>To get a free, no obligation consultation by one of our industry leading experts, as well as a Debt Management Plan simply fill out the form on the right and we will be in contact with you within 48 hours.</p>
  </div>
  <form class="lead-form">
    <header>
      <h3>FREE CONSULTATION</h3>
      <p>Fill in the form below to receive your free, no obligation consultation.</p>
    </header>
    <div class="fields">
      <div class="field"><svg width="12" height="12" viewBox="0 0 12 12"><circle cx="6" cy="4" r="2.5" fill="#9aa2ad"/><path d="M1 12a5 5 0 0 1 10 0z" fill="#9aa2ad"/></svg>Name</div>
      <div class="field"><svg width="12" height="12" viewBox="0 0 12 12"><rect x="3" y="1" width="6" height="10" rx="1" fill="#9aa2ad"/></svg>Phone</div>
      <div class="field"><svg width="12" height="12" viewBox="0 0 12 12"><rect x="1" y="3" width="10" height="7" fill="#9aa2ad"/></svg>E-mail</div>
      <div class="field"><svg width="12" height="12" viewBox="0 0 12 12"><path d="M6 1a3.5 3.5 0 0 1 3.5 3.5C9.5 7 6 11 6 11S2.5 7 2.5 4.5A3.5 3.5 0 0 1 6 1z" fill="#9aa2ad"/></svg>Postcode</div>
      <div class="field"><svg width="12" height="12" viewBox="0 0 12 12"><circle cx="6" cy="6" r="5" fill="#9aa2ad"/></svg>Unsecured Debt</div>
      <div class="field"><svg width="12" height="12" viewBox="0 0 12 12"><circle cx="6" cy="6" r="5" fill="none" stroke="#9aa2ad" stroke-width="1.5"/><path d="M6 3v3l2 1" stroke="#9aa2ad" fill="none"/></svg>Preferred Call time</div>
      <span class="btn">Get my free consultation</span>
    </div>
  </form>
</section>

<section class="services">
  <h2 class="section-title">Here are just some of our Debt Relief Services</h2>
  <div class="service-grid">
    <div class="service">
      <svg width="40" height="40" viewBox="0 0 40 40"><rect x="6" y="10" width="28" height="20" rx="2" fill="none" stroke="#1e2d59" stroke-width="2"/><line x1="6" y1="16" x2="34" y2="16" stroke="#1e2d59" stroke-width="2"/></svg>
      <h4>Dept Consolidation Loans</h4>
      <p>Stop getting hassled by creditors. Let us consolidate your debt into one loan with a single, easy repayment plan.</p>
    </div>
    <div class="service">
      <svg width="40" height="40" viewBox="0 0 40 40"><path d="M6 20 20 8l14 12M10 18v14h20V18" fill="none" stroke="#1e2d59" stroke-width="2"/></svg>
      <h4>Mortgage Refinance</h4>
      <p>Consolidate your debt into available home loan equity, significantly reducing your general repayments.</p>
    </div>
    <div class="service">
      <svg width="40" height="40" viewBox="0 0 40 40"><rect x="10" y="6" width="20" height="28" fill="none" stroke="#1e2d59" stroke-width="2"/><path d="M14 14h12M14 20h12M14 26h8" stroke="#1e2d59" stroke-width="2"/></svg>
      <h4>Debt Agreements</h4>
      <p>A viable alternative to bankruptcy and debt consolidation loans.</p>
    </div>
    <div class="service">
      <svg width="40" height="40" viewBox="0 0 40 40"><circle cx="20" cy="20" r="13" fill="none" stroke="#1e2d59" stroke-width="2"/><path d="m14 20 4 4 8-8" fill="none" stroke="#1e2d59" stroke-width="2"/></svg>
      <h4>Credit Repair</h4>
      <p>Assist you in removing unfair, disputable and incorrect information from your credit file. Information, which you believe should not be there.</p>
    </div>
    <div class="service">
      <svg width="40" height="40" viewBox="0 0 40 40"><path d="M20 6v28M10 12h20M10 12l-5 10h10zM30 12l-5 10h10z" fill="none" stroke="#1e2d59" stroke-width="2"/></svg>
      <h4>Bankruptcy</h4>
      <p>We will work with you to accurately determine if bankruptcy is the sole option for your situation.</p>
    </div>
    <div class="service">
      <svg width="40" height="40" viewBox="0 0 40 40"><rect x="6" y="10" width="28" height="20" rx="2" fill="none" stroke="#1e2d59" stroke-width="2"/><path d="m15 15 10 10M25 15 15 25" stroke="#1e2d59" stroke-width="2"/></svg>
      <h4>Bad credit Loans</h4>
      <p>We work in your best interests to provide a consolidation loan that turns your bad credit history into a positive financial situation.</p>
    </div>
  </div>
  <span class="btn cta">Get my free consultation</span>
</section>

<section class="reviews">
  <h2 class="section-title">Here's What our valued Customers Have to Say About Us</h2>
  <div class="review-grid">
    <article class="review">
      <span class="quote">&ldquo;</span>
      <p>I am very relieved and can now get my life on track. I very sincerely appreciate all of your assistance. You treated me like a person and never condemned me for the situation I was in. If ever I have the opportunity to recommend your services, I will sincerely recommend you. Take care and thank you.</p>
      <div class="reviewer"><span class="avatar" role="img" aria-label="Customer portrait"></span>Karen, Ryde NSW</div>
    </article>
    <article class="review">
      <span class="quote">&ldquo;</span>
      <p>We were on the verge of losing our car and did not know what to do, but now we are in an affordable arrangement to catch up on our payments and are on our way to a debt free future. We are even thinking of buying a house, without your help this would not be possible.</p>
      <div class="reviewer"><span class="avatar" role="img" aria-label="Customer portrait"></span>Paula, Kew VIC</div>
    </article>
    <article class="review">
      <span class="quote">&ldquo;</span>
      <p>I had lost my job and my creditors were about to take legal action against me. I had no idea of what options I had and thought I was going to lose everything. I had worked so hard for, until your help I was able to work out a payment arrangement that everyone could agree to. I would not have known what to do.</p>
      <div class="reviewer"><span class="avatar" role="img" aria-label="Customer portrait"></span>Mark, Blacktown NSW</div>
    </article>
    <article class="review">
      <span class="quote">&ldquo;</span>
      <p>I am writing this letter to express my appreciation for all your help with sorting my finances out. My consultant worked through an easy to understand payment plan which I can easily afford and understand. Thank you.</p>
      <div class="reviewer"><span class="avatar" role="img" aria-label="Customer portrait"></span>Peter, Auburn NSW</div>
    </article>
    <article class="review">
      <span class="quote">&ldquo;</span>
      <p>The previous finance company I went to couldn't consolidate all my debt so put me in worse position. Ledger Advisors stepped in, I am now making only one payment and save me $300 per month.</p>
      <div class="reviewer"><span class="avatar" role="img" aria-label="Customer portrait"></span>Sarah, Gosford NSW</div>
    </article>
    <article class="review">
      <span class="quote">&ldquo;</span>
      <p>Before you will find a selection of client testimonials from satisfied customers all over Australia. These testimonials highlight just how effective a Debt Negotiation debt consolidation loan really is. If you're to become debt free thanks to.</p>
      <div class="reviewer"><span class="avatar" role="img" aria-label="Customer portrait"></span>Mark, Blacktown NSW</div>
    </article>
  </div>
  <span class="btn cta">Get my free consultation</span>
</section>

<footer class="site-footer">
  <span>PRIVACY POLICY</span><span>|</span><span>TERMS AND CONDITIONS</span><span>|</span><span>COPYRIGHTS @ 2015 ALL RIGHTS RESERVED</span>
</footer>
</body>
</html>
```